Company Work Van Design

I am requiring designs for the company work van. The van is a White 2015 Corvane Brisk twin turbo short wheel base. I require all my details on the van. VTRA: 582 4036 M: 0471 865 302 Harbourline Waterproofing Pty Ltd, On the sides i require some dot points for examples of jobs i do. E.g Bathrooms, Balconies, Retaining Walls. Commercial, Residential. Be creative. I will keep updating the project with other details.

Industry/Entity Type

It Company

Colors
cee9f5
85cae6
34a7d8
0493ce
0356a4
3277b5
85acd3
d0dfed
ffffff

```html
<!DOCTYPE html>
<html lang="en">
<head>
<meta charset="utf-8">
<title>Harbourline Waterproofing – Van Wrap Layout</title>
<link href="https://fonts.googleapis.com/css2?family=Roboto+Condensed:wght@400;700&display=swap" rel="stylesheet">
<style>
  :root {
    --bg: #1c1c1c;
    --navy: #0356a4;
    --deep: #2753a3;
    --mid: #3277b5;
    --sky: #34a7d8;
    --bright: #0493ce;
    --pale: #85cae6;
    --ice: #cee9f5;
    --white: #ffffff;
    --tick: #e8572a;
  }
  * { margin: 0; padding: 0; box-sizing: border-box; }
  html, body { width: 1200px; height: 1000px; overflow: hidden; background: var(--bg); }
  body { position: relative; font-family: "Roboto Condensed", Arial, sans-serif; }

  .panel { position: absolute; top: 369px; height: 262px; overflow: hidden; }
  .panel svg.panel-bg { position: absolute; inset: 0; width: 100%; height: 100%; }
  .side-panel { left: 46px; width: 754px; }
  .rear-panel { left: 857px; width: 286px; }

  .water-art { position: absolute; left: 0; top: 70px; width: 300px; height: 120px;
    background: linear-gradient(180deg, rgba(133,202,230,0) 0%, rgba(133,202,230,.35) 45%, rgba(133,202,230,0) 100%); }

  .phone { position: absolute; left: 134px; top: 156px; display: flex; align-items: center; gap: 5px;
    color: var(--white); font-size: 22px; font-weight: 700; letter-spacing: .2px; }
  .phone svg { width: 22px; height: 22px; }

  .licence-badge { position: absolute; left: 277px; top: 115px; width: 37px; height: 32px;
    background: var(--white); border: 1px solid #c9d4e2; }

  .brand { position: absolute; left: 352px; top: 46px; display: flex; align-items: center; gap: 10px; }
  .brand-dot { width: 40px; height: 40px; border-radius: 50%; background: var(--navy); flex: none; }
  .brand-name { color: var(--navy); font-weight: 700; font-size: 19px; line-height: 1.1; text-transform: uppercase; }

  .services { position: absolute; left: 434px; top: 122px; list-style: none; }
  .services li { display: flex; align-items: center; gap: 6px; color: var(--navy);
    font-size: 16px; line-height: 19.5px; }
  .services svg { width: 9px; height: 9px; }
</style>
</head>
<body>

<section class="panel side-panel" aria-label="Van side panel">
  <svg class="panel-bg" viewBox="0 0 754 262" preserveAspectRatio="none" aria-hidden="true">
    <defs>
      <linearGradient id="sideDark" x1="0" y1="0" x2="1" y2="1">
        <stop offset="0" stop-color="#2a58a6"/>
        <stop offset="1" stop-color="#1f5ab0"/>
      </linearGradient>
      <linearGradient id="sideLight" x1="0" y1="0" x2="1" y2="0">
        <stop offset="0.35" stop-color="#85cae6"/>
        <stop offset="0.62" stop-color="#ffffff"/>
      </linearGradient>
    </defs>
    <rect width="754" height="262" fill="url(#sideLight)"/>
    <polygon points="0,0 445,0 228,262 0,262" fill="var(--sky)"/>
    <polygon points="0,0 425,0 208,262 0,262" fill="url(#sideDark)"/>
    <path d="M690,0 C640,60 628,170 660,262 L754,262 L754,0 Z" fill="#2a62ae"/>
    <path d="M672,0 C624,60 612,170 644,262 L650,262 C620,170 632,60 680,0 Z" fill="var(--mid)"/>
  </svg>
  <div class="water-art" role="img" aria-label="Soft blue water wave illustration"></div>
  <div class="phone">
    <svg viewBox="0 0 24 24" aria-hidden="true"><circle cx="12" cy="12" r="11" fill="#fff"/><path d="M8.2 6.5l2 2.2-1 1.4c.8 1.6 2 2.8 3.6 3.6l1.4-1 2.2 2-1 1.9c-4.2-.3-8.2-4.3-8.5-8.5z" fill="#2a58a6"/></svg>
    <span>0471 865 302</span>
  </div>
  <div class="licence-badge" aria-label="Licence badge"></div>
  <div class="brand">
    <span class="brand-dot"></span>
    <span class="brand-name">Harbourline<br>Waterproofing Pty Ltd</span>
  </div>
  <ul class="services">
    <li><svg viewBox="0 0 10 10"><path d="M1 5l3 3 5-7" stroke="var(--tick)" stroke-width="2" fill="none"/></svg>E.g Bathrooms</li>
    <li><svg viewBox="0 0 10 10"><path d="M1 5l3 3 5-7" stroke="var(--tick)" stroke-width="2" fill="none"/></svg>Balconies</li>
    <li><svg viewBox="0 0 10 10"><path d="M1 5l3 3 5-7" stroke="var(--tick)" stroke-width="2" fill="none"/></svg>Retaining Walls</li>
    <li><svg viewBox="0 0 10 10"><path d="M1 5l3 3 5-7" stroke="var(--tick)" stroke-width="2" fill="none"/></svg>Commercial</li>
    <li><svg viewBox="0 0 10 10"><path d="M1 5l3 3 5-7" stroke="var(--tick)" stroke-width="2" fill="none"/></svg>Residential</li>
  </ul>
</section>

<section class="panel rear-panel" aria-label="Van rear panel">
  <svg class="panel-bg" viewBox="0 0 286 262" preserveAspectRatio="none" aria-hidden="true">
    <defs>
      <linearGradient id="rearLight" x1="0" y1="0" x2="0.8" y2="0.6">
        <stop offset="0" stop-color="#34a7d8"/>
        <stop offset="0.55" stop-color="#cee9f5"/>
        <stop offset="1" stop-color="#ffffff"/>
      </linearGradient>
    </defs>
    <rect width="286" height="262" fill="url(#rearLight)"/>
    <rect width="286" height="262" fill="#ffffff" opacity="0.35"/>
    <path d="M0,0 L60,0 C100,80 118,180 112,262 L0,262 Z" fill="#2a62ae"/>
  </svg>
</section>

</body>
</html>
```